Affiliate Flyer

We are looking for a new affiliate flyer. Currently the flyer is based on a black background and we want it to be a cleaner look. We have updated our logo and I include a copy.
I also enclose our current flyer so you can see the content.
This new design needs to be either in a high res PSD, IDML file with full graphics. It is A5.
Some of the wording needs updating so i will list what needs changing:-
Get 5% off fees page:
- selling property for over 8 years, should be 11 years
- saved £20 million pounds, should be £41 million
Smart way to sell your house page:
- 7,000 homes sold, should be 8,500 homes sold
- £20m saved, should be £41m

```html
<!DOCTYPE html>
<html lang="en">
<head>
<meta charset="utf-8">
<title>Affiliate Flyer – Get 5% Off Fees</title>
<link rel="stylesheet" href="https://fonts.googleapis.com/css2?family=Josefin+Sans:wght@200;300&family=Raleway:wght@400;500&family=Oswald:wght@500&display=swap">
<style>
  :root {
    --green-top: #8ec145;
    --green-bottom: #79b03a;
    --quote-box: rgba(255, 255, 255, 0.22);
    --white: #ffffff;
    --panel: #f2f2f2;
    --panel-line: #d9d9d9;
    --ink: #111111;
    --badge: #e2e2e2;
    --brand: #3b3b3b;
  }
  * { margin: 0; padding: 0; box-sizing: border-box; }
  html, body { width: 923px; height: 1200px; overflow: hidden; background: #ffffff; }
  .flyer {
    position: relative;
    width: 923px;
    height: 1200px;
    overflow: hidden;
    font-family: "Raleway", Arial, sans-serif;
  }

  /* Offer section */
  .offer {
    position: absolute;
    left: 0; top: 0;
    width: 923px; height: 763px;
    background: linear-gradient(180deg, var(--green-top) 0%, var(--green-bottom) 100%);
  }
  .offer-visual {
    position: absolute;
    left: 30px; top: 95px;
    width: 610px; height: 415px;
    background: radial-gradient(ellipse at 40% 55%, rgba(110, 159, 52, 0.55) 0%, rgba(120, 176, 58, 0) 70%);
  }
  .offer-headline {
    position: absolute;
    right: 43px; top: 40px;
    text-align: right;
    color: var(--white);
    font-family: "Josefin Sans", "Century Gothic", sans-serif;
    font-weight: 200;
    font-size: 54px;
    line-height: 72px;
    letter-spacing: 9px;
    text-transform: uppercase;
  }
  .quote-code {
    position: absolute;
    left: 525px; top: 193px;
    width: 355px; height: 66px;
    background: var(--quote-box);
  }
  .offer-copy {
    position: absolute;
    left: 51px; top: 500px;
    width: 840px;
    color: var(--white);
    font-size: 17.5px;
    font-weight: 500;
    line-height: 29px;
    text-transform: uppercase;
  }
  .offer-copy p + p { margin-top: 29px; }

  /* Contact section */
  .contact {
    position: absolute;
    left: 0; top: 763px;
    width: 923px; height: 437px;
    background: linear-gradient(180deg, #f6f6f6 0%, var(--panel) 100%);
    border-top: 2px solid var(--panel-line);
  }
  .contact-label {
    position: absolute;
    left: 51px; top: 40px;
    color: var(--ink);
    font-family: "Josefin Sans", "Century Gothic", sans-serif;
    font-weight: 300;
    font-size: 36px;
    letter-spacing: 5.6px;
    text-transform: uppercase;
  }
  .contact-phone {
    position: absolute;
    left: 51px; top: 96px;
    color: var(--ink);
    font-family: "Oswald", "Arial Narrow", sans-serif;
    font-weight: 500;
    font-size: 58px;
    line-height: 1;
    letter-spacing: 11px;
  }
  .listings {
    position: absolute;
    left: 0; top: 189px;
    width: 923px; height: 127px;
    border-top: 1px solid #e6e6e6;
    border-bottom: 2px solid var(--panel-line);
  }
  .listing-badge {
    position: absolute;
    top: 30px;
    height: 58px;
    background: var(--badge);
    border-radius: 4px;
  }
  .listing-badge--one { left: 112px; width: 208px; }
  .listing-badge--two { left: 340px; width: 195px; }
  .listing-badge--three { left: 553px; width: 282px; }

  .brand {
    position: absolute;
    right: 43px; top: 335px;
    display: flex;
    align-items: center;
    gap: 14px;
  }
  .brand-mark {
    width: 72px; height: 72px;
    background: var(--brand);
  }
  .brand-name {
    color: var(--brand);
    font-family: "Raleway", Arial, sans-serif;
    font-weight: 500;
    font-size: 30px;
    line-height: 32px;
    text-transform: uppercase;
  }
  .brand-tagline {
    display: block;
    font-size: 16px;
    line-height: 22px;
    text-transform: none;
    letter-spacing: 1px;
  }
</style>
</head>
<body>
  <main class="flyer">
    <section class="offer">
      <div class="offer-visual" role="img" aria-label="Faded illustration of a house with a For Sale sign in front"></div>
      <h1 class="offer-headline">Get 5% off fees<br>by quoting</h1>
      <div class="quote-code" aria-label="Space for the affiliate quote code"></div>
      <div class="offer-copy">
        <p>If you're looking for a modern, established, low cost and proven method of estate agency then look no further – for a fee of &nbsp;£495 + VAT we can sell your home.</p>
        <p>We've been selling property for over 11 years, successfully completing on thousands of sales nationwide and delivering a service that's modernized estate agency, and saved over &nbsp;£41 million pounds in traditional agency fees.</p>
      </div>
    </section>

    <section class="contact">
      <h2 class="contact-label">Call for more information</h2>
      <p class="contact-phone">0845 246 810</p>
      <div class="listings" aria-label="Property listing partners">
        <div class="listing-badge listing-badge--one"></div>
        <div class="listing-badge listing-badge--two"></div>
        <div class="listing-badge listing-badge--three"></div>
      </div>
      <div class="brand">
        <div class="brand-mark"></div>
        <p class="brand-name">Homestead<br>Link<span class="brand-tagline">where smart sellers start</span></p>
      </div>
    </section>
  </main>
</body>
</html>
```